Stationary Design to Complement our Website

We would like template designed for word documents that we can use for headed paper. The template should complement the style of our website & incorporate our existing logo. https://www.velmorantravel.com/

The header and footer design should be sperate PNG or JPEG files that we can copy and paste into word header and footers. They should work on A4 & letter sized papers.

Note the main web colours are as follows:

Black
HEX code #2b2c2b
C=71 M=64 Y=64 K=65
RGB 43,44,43

Green
HEX code #116c49
C=88 M=33 Y=82 K=24
RGB 17,108,73

Current fonts are ALEO & Gilroy.

Fonts and colours in new design don't have to match website exactly but should be complementary.

Font styles to use
Serif

Requirements
Must have
• a simple design that complements our website.
Some kind of graphic on the top & some sort of graphic on the bottom. Not just plain logo on top.
designs that incorporate the clouds might look good
Can also incorporate 5* rate harbor rating
Should not have
• no photographs included on the design

```html
<!DOCTYPE html>
<html lang="en">
<head>
<meta charset="utf-8">
<title>Velmoran Travel Letterhead</title>
<link rel="stylesheet" href="https://fonts.googleapis.com/css2?family=Cinzel:wght@500&family=Libre+Baskerville:ital@0;1&family=Outfit:wght@700&display=swap">
<style>
  :root {
    --olive: #8ba54e;
    --green: #116c49;
    --ink: #1d1d1d;
    --body: #5c5c5c;
    --rule: #d6d6d6;
    --white: #ffffff;
  }
  * { margin: 0; padding: 0; box-sizing: border-box; }
  html, body { width: 927px; height: 1200px; overflow: hidden; background: var(--white); }
  .letterhead { position: relative; width: 927px; height: 1200px; overflow: hidden; font-family: "Libre Baskerville", Georgia, serif; }

  .contact-bar {
    position: absolute; top: 0; left: 0; width: 100%; height: 52px;
    background: var(--olive); color: var(--white);
    display: flex; align-items: center; justify-content: center; gap: 18px;
    font-family: "Libre Baskerville", Georgia, serif; font-size: 13.5px; letter-spacing: 2.6px;
  }

  .brand {
    position: absolute; top: 118px; left: 0; width: 100%;
    display: flex; justify-content: center; align-items: center; gap: 14px;
  }
  .brand-dot { width: 16px; height: 16px; border-radius: 50%; background: var(--green); }
  .brand-name {
    font-family: "Cinzel", "Times New Roman", serif; font-weight: 500;
    font-size: 36px; letter-spacing: 7px; color: var(--ink);
  }

  .divider { position: absolute; top: 247px; left: 103px; width: 714px; height: 1.5px; background: var(--rule); }
  .divider-accent { position: absolute; top: 242px; left: 318px; width: 285px; height: 12px; background: var(--green); }

  .letter { position: absolute; top: 342px; left: 137px; width: 653px; color: var(--body); }
  .letter-date { text-align: right; font-size: 12.5px; }
  .letter-greeting { margin-top: 24px; font-size: 19px; color: var(--ink); }
  .letter-body { margin-top: 16px; }
  .letter-body p { font-size: 11.3px; line-height: 20.3px; text-align: justify; margin-bottom: 20.3px; }

  .signature-mark { position: absolute; top: 873px; left: 137px; width: 163px; height: 54px; background: #f1f1f1; border-radius: 3px; }
  .signatory { position: absolute; top: 940px; left: 137px; color: var(--body); }
  .signatory-name { font-size: 16px; }
  .signatory-role { font-style: italic; font-size: 10.5px; margin-top: 6px; }

  .footer-band {
    position: absolute; top: 1062px; left: 0; width: 100%; height: 138px;
    background: linear-gradient(to bottom, rgba(17,108,73,0) 0%, rgba(17,108,73,0.55) 35%, rgba(17,108,73,0.92) 70%, var(--green) 100%);
  }
  .tagline-row {
    position: absolute; top: 1119px; left: 0; width: 100%; height: 40px;
    display: flex; align-items: center;
  }
  .tagline-line { height: 1.5px; background: var(--white); flex: 1; }
  .tagline {
    padding: 0 18px; color: var(--white);
    font-family: "Outfit", Arial, sans-serif; font-weight: 700; font-size: 33px; letter-spacing: 0.2px; white-space: nowrap;
  }
</style>
</head>
<body>
<div class="letterhead">
  <header class="contact-bar">
    <span>info@velmorantravel.com</span><span>|</span>
    <span>Toll Free +1 877-555-0142</span><span>|</span>
    <span>www.velmorantravel.com</span>
  </header>

  <div class="brand">
    <span class="brand-dot"></span>
    <span class="brand-name">VELMORAN TRAVEL</span>
  </div>

  <div class="divider"></div>
  <div class="divider-accent"></div>

  <main class="letter">
    <p class="letter-date">3, February 2021</p>
    <p class="letter-greeting">Hello,</p>
    <div class="letter-body">
      <p>Lorem ipsum dolor sit amet, consectetur adipiscing elit. Integer et aliquet risus. Suspendisse mattis justo id velit mollis ullamcorper. Integer fermentum ornare egestas. Nunc facilisis enim id metus tempor, ac auctor velit iaculis. Integer semper rutrum volutpat. Donec ut lacinia tortor. Integer maximus nulla vel ante pretium maximus.</p>
      <p>Vestibulum ante ipsum primis in faucibus orci luctus et ultrices posuere cubilia Curae; Donec lobortis quam ac mi aliquam, sed lacinia ligula cursus. Pellentesque ac velit sed lacus varius volutpat sit amet at sapien. Vivamus nec tempus ante. Donec volutpat diam et nibh lacinia, sit amet pulvinar dui vestibulum. Donec lobortis quam ac mi aliquam, sed lacinia ligula cursus. Fusce eget ipsum id libero facilisis ornare sed blandit sapien. Vestibulum ante ipsum primis in faucibus orci luctus et ultrices posuere cubilia Cura</p>
      <p>Vestibulum ante ipsum primis in faucibus orci luctus et ultrices posuere cubilia Curae; Donec lobortis quam ac mi aliquam, sed lacinia ligula cursus. Pellentesque ac velit sed lacus varius volutpat sit amet at sapien. Vivamus nec tempus ante. Donec volutpat diam et nibh lacinia, sit amet pulvinar dui vestibulum. Fusce eget ipsum id libero facilisis ornare sed blandit sapien. Vestibulum ante ipsum primis in faucibus orci luctus et ultrices posuere cubilia Curae. Nunc a commodo erat.</p>
      <p>In nec egestas purus, vehicula porttitor nunc. Donec faucibus velit nec lobortis hendrerit. Donec volutpat diam et nibh lacinia, sit amet pulvinar dui vestibulum. Fusce eget ipsum id libero facilisis ornare sed blandit sapien. Vestibulum ante ipsum primis in faucibus orci luctus et ultrices posuere cubilia Curae. Nunc a commodo erat. In nec egestas purus.</p>
    </div>
  </main>

  <div class="signature-mark" role="img" aria-label="Handwritten signature"></div>
  <div class="signatory">
    <p class="signatory-name">Name ,Surname</p>
    <p class="signatory-role">General Manager.</p>
  </div>

  <footer class="footer-band"></footer>
  <div class="tagline-row">
    <span class="tagline-line"></span>
    <span class="tagline">Experience Ireland like a local.</span>
    <span class="tagline-line"></span>
  </div>
</div>
</body>
</html>
```